Introduction flyer

Bright Harvest Nutrition & Wellness Consulting, is a new holistic nutritional therapy specialising in womens health. I want a flyer that appeals to women between 15 to 60. It must speak "health, food & balance". I have attached the basic info I need included in the text. I like Greens & Blues, soft text. My flyer will be distributed to cafes, shops, fitness centres, hung up in grocery stores & health centres etc. The QERV & DLUP logos need to appear on the flyer to show I am fully registered. My own logo & company name is attached.

Target Market(s)

Women from 10 to 60 years old.

Industry/Entity Type

Nutritionist

Colors
32a6d7
abd037
33b8a4
fbf289
ffcf3e
b768aa
d5d5d5
dcdcdc
e8e8e8

Requirements
Must have
• An image of healthy food & ladies. A group of women eating soup, stews or curry type dishes, with plenty of colour - no bread or white wine, and not just fruit please. Food that looks enjoyable to the average person.
• Nutrition is main part of my job, so please keep that in mind & emphasise food & natural well being.
Should not have
• People exercising, men, white wine, bread, cakes, sweets etc..

```html
<!DOCTYPE html>
<html lang="en">
<head>
<meta charset="utf-8">
<title>Bright Harvest Nutrition &amp; Wellness Consulting – Flyer</title>
<link href="https://fonts.googleapis.com/css2?family=Cinzel:wght@600;700&family=Tinos:wght@400;700&display=swap" rel="stylesheet">
<style>
  :root{
    --page-bg:#a3a3a3;
    --leaf-light:#a9d86a;
    --leaf:#6cc04a;
    --leaf-deep:#3f9a3a;
    --teal:#17a39c;
    --teal-dark:#0f8f89;
    --teal-light:#52c1bc;
    --white:#ffffff;
    --ink:#111111;
    --alert-red:#e3141b;
    --sun-yellow:#ffe93a;
    --brand-blue:#2a6fb0;
    --brand-green:#1f8d3b;
  }
  *{box-sizing:border-box;margin:0;padding:0}
  html,body{width:1200px;height:1000px;overflow:hidden}
  body{background:var(--page-bg);font-family:"Tinos",serif;position:relative}
  .flyer{position:absolute;left:297px;top:57px;width:648px;height:885px;background:var(--white);overflow:hidden}
  .flyer-shapes{position:absolute;inset:0}
  .abs{position:absolute}
  .headline{left:36px;top:40px;font-family:"Cinzel",serif;font-weight:700;font-size:34px;color:var(--alert-red);letter-spacing:.5px}
  .symptoms{left:58px;top:100px;color:var(--white);font-size:24px;line-height:28px}
  .baby-question{left:33px;top:226px;font-family:"Cinzel",serif;font-weight:600;font-size:20px;color:var(--white);letter-spacing:1px}
  .specialities-title{left:100px;top:355px;width:162px;text-align:right;font-weight:700;font-size:24px;line-height:31px;color:var(--sun-yellow)}
  .speciality{position:absolute;left:0;display:flex;align-items:center;font-size:13px;line-height:16px}
  .speciality.is-ticked{color:var(--white)}
  .speciality.is-bold{color:var(--ink);font-weight:700;padding-left:51px}
  .tick{width:23px;height:23px;margin:0 18px 0 10px;flex:none}
  .contact-bar{left:0;top:816px;width:200px;height:22px;background:var(--teal-dark);color:var(--sun-yellow);font-family:"Cinzel",serif;font-weight:700;font-size:14px;text-align:center;line-height:22px}
  .call-box{left:216px;top:813px;width:118px;height:40px;border:2px solid var(--teal-dark);background:var(--teal);color:var(--sun-yellow);font-family:"Cinzel",serif;font-size:13px;line-height:16px;padding:3px 6px}
  .call-box .phone{font-family:"Tinos",serif;font-size:15px}
  .email{left:20px;top:848px;color:var(--sun-yellow);font-family:"Cinzel",serif;font-size:13px;line-height:17px}
  .home-visits{left:548px;top:316px;width:100px;color:var(--sun-yellow);font-family:"Cinzel",serif;font-weight:600;font-size:12.5px;line-height:16px}
  .brand{left:295px;top:325px;width:240px;text-align:center;color:var(--brand-blue);font-weight:700;font-size:19px;line-height:23px;letter-spacing:.5px}
  .brand-mark{width:70px;height:70px;border-radius:50%;background:var(--brand-green);margin:0 auto 40px}
  .tagline{left:300px;top:556px;width:300px;text-align:center;color:var(--brand-blue);font-weight:700;font-size:16.5px;line-height:21px}
  .about{left:335px;top:616px;width:300px;text-align:center;color:var(--brand-green);font-size:13px;line-height:16.2px}
  .registered{left:358px;top:791px;width:290px;height:24px;background:var(--teal);color:var(--white);font-weight:700;font-size:16px;line-height:24px;padding-left:92px}
  .register-mark{display:flex;align-items:center;gap:7px;font-weight:700;font-size:22px}
  .register-mark i{display:block;width:22px;height:22px;border-radius:50%}
  .mark-dlup{left:405px;top:835px;color:var(--teal)}
  .mark-dlup i{background:var(--teal)}
  .mark-qerv{left:515px;top:835px;color:#5b3d8e}
  .mark-qerv i{background:#5b3d8e}
</style>
</head>
<body>
<main class="flyer">
  <svg class="flyer-shapes" width="648" height="885" viewBox="0 0 648 885" aria-hidden="true">
    <defs>
      <radialGradient id="photo-glow" cx="0.75" cy="0.25" r="0.9">
        <stop offset="0" stop-color="#d3eab5"/>
        <stop offset=".45" stop-color="#8ccd5d"/>
        <stop offset="1" stop-color="#4fae3e"/>
      </radialGradient>
    </defs>
    <rect x="0" y="0" width="648" height="380" fill="url(#photo-glow)"/>
    <path d="M0,330 C120,300 230,280 340,282 L340,400 L0,400 Z" fill="var(--leaf-light)"/>
    <path d="M0,350 C120,330 230,308 320,300 L320,885 L0,885 Z" fill="var(--teal)"/>
    <path d="M532,275 L648,275 L648,500 C620,520 590,500 560,515 L532,520 Z" fill="var(--teal)"/>
    <path d="M300,300 C380,272 470,272 532,290 L532,520 L560,515 C590,500 620,520 648,500 L648,885 L355,885 C330,820 335,760 348,700 C362,620 285,560 272,470 C262,390 272,330 300,300 Z" fill="var(--white)"/>
    <rect x="0" y="435" width="285" height="58" fill="var(--teal-light)"/>
    <rect x="0" y="495" width="282" height="60" fill="var(--teal-light)"/>
    <rect x="0" y="563" width="280" height="35" fill="var(--teal-light)"/>
    <rect x="0" y="634" width="280" height="34" fill="var(--teal-light)"/>
    <rect x="0" y="700" width="285" height="34" fill="var(--teal-light)"/>
    <rect x="0" y="770" width="330" height="42" fill="var(--teal-light)"/>
  </svg>
  <div class="abs" role="img" aria-label="Photo of smooth stacked stones on a wooden board against a soft green garden background" style="left:455px;top:60px;width:193px;height:230px"></div>

  <h1 class="abs headline">Do you experience</h1>
  <p class="abs symptoms">Low energy,<br>Low libido,<br>Menstrual cycle complications,</p>
  <p class="abs baby-question">or are you planning a baby?</p>

  <h2 class="abs specialities-title">Our<br>Specialities</h2>
  <ul class="specialities">
    <li class="speciality is-ticked" style="top:443px"><svg class="tick" viewBox="0 0 24 24"><circle cx="12" cy="12" r="11" fill="#fff"/><path d="M6.5 12.5l4 4 7-8" fill="none" stroke="var(--teal)" stroke-width="3"/></svg>Fertility, IVF, pre-conception,<br>pregnancy &amp; post-natal care</li>
    <li class="speciality is-bold" style="top:502px">Menstrual cycle challenges<br>(PCOS, Endometriosis, PMS,<br>heavy/irregular periods etc)</li>
    <li class="speciality is-ticked" style="top:568px"><svg class="tick" viewBox="0 0 24 24"><circle cx="12" cy="12" r="11" fill="#fff"/><path d="M6.5 12.5l4 4 7-8" fill="none" stroke="var(--teal)" stroke-width="3"/></svg>Thyroid conditions</li>
    <li class="speciality is-bold" style="top:606px">Low libido</li>
    <li class="speciality is-ticked" style="top:639px"><svg class="tick" viewBox="0 0 24 24"><circle cx="12" cy="12" r="11" fill="#fff"/><path d="M6.5 12.5l4 4 7-8" fill="none" stroke="var(--teal)" stroke-width="3"/></svg>Digestive health</li>
    <li class="speciality is-bold" style="top:675px">Chronic fatigue syndrome</li>
    <li class="speciality is-ticked" style="top:705px"><svg class="tick" viewBox="0 0 24 24"><circle cx="12" cy="12" r="11" fill="#fff"/><path d="M6.5 12.5l4 4 7-8" fill="none" stroke="var(--teal)" stroke-width="3"/></svg>Perimenopause/menopause</li>
    <li class="speciality is-bold" style="top:743px">Weight management</li>
    <li class="speciality is-ticked" style="top:775px"><svg class="tick" viewBox="0 0 24 24"><circle cx="12" cy="12" r="11" fill="#fff"/><path d="M6.5 12.5l4 4 7-8" fill="none" stroke="var(--teal)" stroke-width="3"/></svg>Type 2 diabetes, blood sugar dysregulation,<br>high blood pressure, high cholesterol</li>
  </ul>

  <div class="abs contact-bar">Contact me</div>
  <div class="abs call-box">Call Maeve:<br><span class="phone">085-4402-816</span></div>
  <p class="abs email">Email:<br>maeve@brightharvestnutrition.ie</p>

  <p class="abs home-visits">Home visits available, at no extra cost within local area; I can visit your place of work or home.</p>

  <div class="abs brand">
    <div class="brand-mark"></div>
    BRIGHT HARVEST NUTRITION<br>&amp;<br>Wellness Consulting
  </div>

  <p class="abs tagline">Small changes to your diet may lead<br>to big changes in your health.</p>
  <p class="abs about">Eat well, live well. Discover exactly what YOU need to change and how to make these changes long lasting. There is no 1 rule-fits-all. My nutritional advice aims to dig up the root cause to my client’s health concerns. My lifestyle plans are completely personalised to an individual’s needs and circumstances. I consider the whole person not just symptoms or disease.</p>

  <div class="abs registered">Registered with:</div>
  <div class="abs register-mark mark-dlup"><i></i>DLUP</div>
  <div class="abs register-mark mark-qerv"><i></i>QERV</div>
</main>
</body>
</html>
```